Lorvika.no is a new website about pedagogical entrepreneurship. It's main target group is teachers. The Fjellmark Institute for Classroom Media and the Nordvik Agency for Schools and Study are leading the project.

The web page is meant to show examples of how different methods of entrepreneurship can be used pedagogical in a learning environment. The page will also support the user with examples of different teaching programs and other examples of best practice.

Pedagogical entrepreneurship is not about business and men in suits. It's a method for learning. The focus in the design should be on school, education and new ways of learning.

The final product should be motivating and engaging, but at the same time governmental and serious. We are not looking for something "flashy" and corporate-looking, but a moderate, task-focused and clean design that state quality.

We need designs for three pages:
1 - frontpage
2 - subpage ("Metoder og undervisningsopplegg")
3 - subpage ("Smått-VERK i Brekkelia")

The interaction design for these three pages will be uploaded as an attachment.

We would like you to find inspiration in the following websites:
- www.gryvekst.no
- www.lavrek.no
- www.tovandstudio.com
- www.kvp.no
(more will be added)

Please use the attached logo, and feel free to use this as an inspiration for the rest of the design.

Target Market(s)

Teachers

Industry/Entity Type

Education

Requirements
Must have
• * Header with: Logo. Main navigation. Utility navigation. Search box.
* Footer
Should not have
• Images of men in suits.
Very strong graphical elements that stands out too much (we want it clean).

```html
<!DOCTYPE html>
<html lang="en">
<head>
<meta charset="utf-8">
<title>Lorvika.no – Pedagogical Entrepreneurship</title>
<link href="https://fonts.googleapis.com/css2?family=Fira+Sans+Condensed:ital,wght@0,400;0,500;0,600;0,700;1,500;1,600;1,700&family=Arimo:wght@400;700&display=swap" rel="stylesheet">
<style>
:root{
  --navy:#0b4a7a;
  --navy-deep:#0a4373;
  --blue:#1e7cc4;
  --sky:#5aaee3;
  --sky-light:#6fbcec;
  --heading-blue:#4a9ad8;
  --ink:#6f6f6f;
  --link-red:#a01818;
  --nav-grey:#9a9a9a;
  --placeholder-light:#f1f1f1;
  --placeholder-mid:#d6d6d6;
  --white:#ffffff;
  --cond:"Fira Sans Condensed", sans-serif;
  --plain:"Arimo", Arial, sans-serif;
}
*{box-sizing:border-box;margin:0;padding:0}
html,body{width:859px;height:1200px;overflow:hidden;background:var(--white)}
body{position:relative;font-family:var(--cond);color:var(--ink)}
.abs{position:absolute}

/* header */
.site-header{position:absolute;left:0;top:0;width:859px;height:224px;
  background:linear-gradient(90deg,var(--navy-deep) 0%,#105592 38%,#2f82c4 62%,var(--sky-light) 100%)}
.search-box{position:absolute;left:640px;top:8px;width:124px;height:14px;background:var(--white);border-radius:7px}
.search-box svg{position:absolute;right:5px;top:1px}
.brand{position:absolute;left:88px;top:92px;display:flex;align-items:center;gap:8px}
.brand-dot{width:40px;height:40px;border-radius:50%;background:var(--white);opacity:.9}
.brand-name{font-family:var(--cond);font-weight:600;font-size:30px;color:var(--white);letter-spacing:.5px}
.promo{position:absolute;top:40px;width:164px;height:164px}
.promo-1{left:266px}.promo-2{left:436px}.promo-3{left:608px}
.promo-label{position:absolute;left:22px;width:120px;top:52px;height:72px;display:flex;align-items:center;justify-content:center;text-align:center;
  color:var(--white);font-weight:600;font-size:13.5px;line-height:21px}

/* main nav */
.main-nav{position:absolute;left:0;top:224px;width:859px;height:30px;
  background:linear-gradient(#fafafa,#e6e6e6);border-bottom:1px solid #d4d4d4}
.main-nav ul{list-style:none;display:flex;position:absolute;left:77px;top:0;height:30px}
.main-nav li{font-style:italic;font-weight:500;font-size:16px;letter-spacing:-.4px;color:var(--nav-grey);padding:0 14px;line-height:30px;border-right:1px solid #d0d0d0}
.main-nav li:last-child{border-right:none}
.main-nav li.current{color:var(--blue);font-weight:600}

/* intro */
.intro-title{left:92px;top:288px;font-size:18px;font-weight:600;letter-spacing:-.1px;color:var(--heading-blue)}
.follow{left:648px;top:290px;display:flex;align-items:center;gap:3px}
.follow span{font-size:10px;font-style:italic;font-weight:600;color:var(--heading-blue);margin-right:6px}
.follow i{display:block;width:15px;height:15px;background:var(--heading-blue);border-radius:2px}
.follow i:nth-child(4){background:#b22}.follow i:nth-child(5){background:#e9822c}
.intro-text{left:92px;top:316px;width:678px;font-size:12px;font-weight:600;letter-spacing:-.25px;line-height:21.2px;color:var(--ink);text-align:justify}
.learn-more{left:718px;top:425px;font-size:12.5px;font-weight:600;color:var(--heading-blue)}

/* meter card */
.meter-card{left:91px;top:460px;width:154px;height:184px;background:linear-gradient(#1b6fb4,#0b4a7a);border-radius:4px;box-shadow:0 2px 4px rgba(0,0,0,.35)}
.meter-card h3{color:var(--white);font-weight:500;font-size:13.5px;line-height:17px;text-align:center;margin-top:5px}
.meter-inner{position:absolute;left:5px;top:43px;width:144px;height:134px;background:var(--white);border-radius:3px}
.meter-art{position:absolute;left:14px;top:8px;width:116px;height:94px;border-radius:4px;background:linear-gradient(var(--placeholder-light),var(--placeholder-mid))}
.meter-link{position:absolute;left:0;right:0;bottom:8px;text-align:center;font-size:14.5px;font-weight:600;letter-spacing:-.2px;color:var(--link-red);text-decoration:underline}

/* get started */
.start-btn{left:270px;top:459px;width:186px;height:35px;border-radius:4px;background:linear-gradient(#8a8a8a,#5b5b5b);color:var(--white);
  font-family:var(--plain);font-weight:700;font-size:14px;line-height:35px;padding-left:40px;z-index:2}
.start-btn svg{position:absolute;left:0;top:0}
.start-panel{left:279px;top:495px;width:411px;height:147px;border:1px solid #ddd;border-radius:6px;background:linear-gradient(#f7f1ee,#fff 40%)}
.start-col{position:absolute;top:14px;font-family:var(--plain);font-size:10px;line-height:16.5px;color:#555}
.start-col h4{font-size:11px;font-weight:700;color:#555;margin-bottom:6px}
.start-col .more{color:var(--link-red);text-decoration:underline}

/* inspiration */
.inspo-title{left:97px;top:670px;font-size:23px;font-weight:700;color:var(--navy);letter-spacing:0}
.carousel{left:97px;top:706px;width:661px;height:145px;background:var(--white);box-shadow:0 1px 5px rgba(0,0,0,.45)}
.carousel .arrow{position:absolute;top:57px}
.slide{position:absolute;top:12px;width:134px;text-align:center}
.slide-photo{width:134px;height:92px;border:2px solid #eee;background:linear-gradient(#d9e4ee,#c4b6aa 60%,#e8ecef)}
.slide-caption{margin-top:4px;font-size:13.5px;font-weight:500;line-height:16px;color:var(--blue)}

/* footer */
.footer-nav{position:absolute;left:0;top:887px;width:859px;height:40px;background:var(--sky)}
.footer-nav ul{list-style:none;display:flex;position:absolute;left:100px;top:0;line-height:40px}
.footer-nav li{color:var(--white);font-style:italic;font-weight:600;font-size:14px;margin-right:22px}
.site-footer{position:absolute;left:0;top:927px;width:859px;height:273px;background:var(--navy);font-family:var(--plain);color:var(--white)}
.footer-brand{position:absolute;left:92px;top:22px;display:flex;flex-direction:column;align-items:center;gap:8px}
.footer-brand .brand-dot{width:52px;height:52px}
.footer-brand .brand-name{font-size:18px}
.footer-col{position:absolute;top:19px;font-size:10px;line-height:16.5px}
.footer-col h4{font-size:11.5px;font-weight:700;margin-bottom:6px}
.footer-col .more{text-decoration:underline}
.contact{position:absolute;top:134px;left:191px;font-size:10px;line-height:17px}
.contact h4{font-size:11.5px;font-weight:700;margin-bottom:4px}
.contact .cols{display:flex;gap:15px}
.copyright{position:absolute;left:86px;top:253px;font-size:10px}
</style>
</head>
<body>

<header class="site-header">
  <div class="search-box" role="search">
    <svg width="14" height="12" viewBox="0 0 14 12"><circle cx="5" cy="5" r="3.5" fill="none" stroke="#1e7cc4" stroke-width="1.5"/><line x1="7.6" y1="7.4" x2="11" y2="10.5" stroke="#1e7cc4" stroke-width="2"/></svg>
  </div>
  <div class="brand"><span class="brand-dot"></span><span class="brand-name">Lorvika</span></div>

  <a class="promo promo-1">
    <svg width="164" height="164" viewBox="0 0 164 164">
      <defs><path id="arc1" d="M22,104 A64,64 0 1 1 142,104"/></defs>
      <circle cx="82" cy="82" r="80" fill="#fff"/>
      <circle cx="82" cy="94" r="60" fill="#1e7cc4"/>
      <text font-family="Fira Sans Condensed, sans-serif" font-weight="700" font-size="12.5" fill="#1e7cc4"><textPath href="#arc1" startOffset="50%" text-anchor="middle">LEARN ABOUT WHAT, WHY AND HOW!</textPath></text>
    </svg>
    <span class="promo-label">What is<br>pedagocial<br>entrepreneurship?</span>
  </a>
  <a class="promo promo-2">
    <svg width="164" height="164" viewBox="0 0 164 164">
      <defs><path id="arc2" d="M22,104 A64,64 0 1 1 142,104"/></defs>
      <circle cx="82" cy="82" r="80" fill="#fff"/>
      <circle cx="82" cy="94" r="60" fill="#1e7cc4"/>
      <text font-family="Fira Sans Condensed, sans-serif" font-weight="700" font-size="12.5" fill="#1e7cc4"><textPath href="#arc2" startOffset="50%" text-anchor="middle">PLAN YOUR LESSONS</textPath></text>
    </svg>
    <span class="promo-label">Methods<br>&amp;<br>Teaching Plans</span>
  </a>
  <a class="promo promo-3">
    <svg width="164" height="164" viewBox="0 0 164 164">
      <defs><path id="arc3" d="M22,104 A64,64 0 1 1 142,104"/></defs>
      <circle cx="82" cy="82" r="80" fill="#fff"/>
      <circle cx="82" cy="94" r="60" fill="#1e7cc4"/>
      <text font-family="Fira Sans Condensed, sans-serif" font-weight="700" font-size="12.5" fill="#1e7cc4"><textPath href="#arc3" startOffset="50%" text-anchor="middle">BE INSPIRED</textPath></text>
    </svg>
    <span class="promo-label">Good Example<br>&amp;<br>Best Practice</span>
  </a>
</header>

<nav class="main-nav">
  <ul>
    <li class="current">Home</li><li>About Lorvika</li><li>Best Practice Schools</li><li>Lorvikameter</li><li>Teaching Plans</li><li>Methods</li>
  </ul>
</nav>

<h1 class="abs intro-title">Pedagocial Entrepreneurship Works</h1>
<div class="abs follow"><span>Follow Us</span><i aria-label="Social link"></i><i aria-label="Social link"></i><i aria-label="Video link"></i><i aria-label="Feed link"></i></div>
<p class="abs intro-text">Lorem ipsum dolor sit amet, consectetur adipiscing elit. Morbi iaculis pretium leo, eu faucibus urna ultricies non. Vestibulum eget augue quam, nec tristique neque. Curabitur semper arcu feugiat mi scelerisque id vehicula sem convallis. Phasellus at diam eget ligula pretium blandit vel et ante. Integer vestibulum congue nisl, congue aliquet dolor fringilla non. Nullam dictum dapibus felis, non tincidunt ipsum vulputate ut. Pellentesque eu fringilla ante. Proin ullamcorper mattis diam et consequat. Nulla facilisi. Phasellus risus ligula, elementum et blandit non, lacinia vel nunc. In blandit ipsum id dolor interdum auctor.</p>
<a class="abs learn-more">Learn More</a>

<aside class="abs meter-card">
  <h3>Are You working<br>Entrepreneurship-like?</h3>
  <div class="meter-inner">
    <div class="meter-art" role="img" aria-label="Illustration of a dial gauge measuring entrepreneurial teaching"></div>
    <span class="meter-link">Try the Lorvikameter</span>
  </div>
</aside>

<div class="abs start-btn">
  <svg width="36" height="35" viewBox="0 0 36 35"><path d="M6 8 H20 V3 L33 17.5 L20 32 V27 H6 Z" fill="#b5b5b5" stroke="#777" stroke-width="1"/></svg>
  GET STARTED NOW
</div>
<div class="abs start-panel">
  <div class="start-col" style="left:17px">
    <h4>Methods</h4>
    Cafe Pedagogikk<br>Elevbedriff<br>Story Line<br>Real<br>Cafe-Pedagogic<br><span class="more">See More...</span>
  </div>
  <div class="start-col" style="left:127px">
    <h4>Teaching Plans</h4>
    Plan 1<br>Plan 2<br>Plan 3<br>Plan 4<br>Plan 5<br><span class="more">See More...</span>
  </div>
</div>

<h2 class="abs inspo-title">INSPIRATION</h2>
<section class="abs carousel">
  <svg class="arrow" style="left:6px" width="14" height="24" viewBox="0 0 14 24"><path d="M11 2 L3 12 L11 22" fill="none" stroke="#666" stroke-width="3"/></svg>
  <div class="slide" style="left:37px"><div class="slide-photo" role="img" aria-label="Photo of a school building with pupils in the snowy yard"></div><p class="slide-caption">Smått-VERK at<br>Brekkelia School</p></div>
  <div class="slide" style="left:186px"><div class="slide-photo" role="img" aria-label="Photo of a school building with pupils in the snowy yard"></div><p class="slide-caption">Smått-VERK at<br>Brekkelia School</p></div>
  <div class="slide" style="left:335px"><div class="slide-photo" role="img" aria-label="Photo of a school building with pupils in the snowy yard"></div><p class="slide-caption">Smått-VERK at<br>Brekkelia School</p></div>
  <div class="slide" style="left:486px"><div class="slide-photo" role="img" aria-label="Photo of a school building with pupils in the snowy yard"></div><p class="slide-caption">Smått-VERK at<br>Brekkelia School</p></div>
  <svg class="arrow" style="left:641px" width="14" height="24" viewBox="0 0 14 24"><path d="M3 2 L11 12 L3 22" fill="none" stroke="#666" stroke-width="3"/></svg>
</section>

<nav class="footer-nav">
  <ul><li>Home</li><li>About Lorvika</li><li>Best Practice Schools</li><li>Lorvikameter</li><li>Teaching Plans</li><li>Methods</li><li>Contact Us</li></ul>
</nav>

<footer class="site-footer">
  <div class="footer-brand"><span class="brand-dot"></span><span class="brand-name">Lorvika</span></div>
  <div class="footer-col" style="left:191px">
    <h4>Pedagogical Entrepreneurship</h4>
    What is pedagogical entrepreneurship?<br>Science<br>Best Practice Schools<br>Lorvikameteret
  </div>
  <div class="footer-col" style="left:392px">
    <h4>Methods</h4>
    Story Line<br>Real<br>Cafe-Pedagogic<br><span class="more">See More...</span>
  </div>
  <div class="footer-col" style="left:505px">
    <h4>Gode Eksempler</h4>
    Smått-VERK at Brekkelia School<br>Smått-VERK at Brekkelia School<br>Smått-VERK at Brekkelia School<br><span class="more">See More...</span>
  </div>
  <div class="footer-col" style="left:669px">
    <h4>Teaching Plans</h4>
    Tincidunt libero 1<br>Tincidunt libero 2<br>Tincidunt libero 3<br><span class="more">See More...</span>
  </div>
  <div class="contact">
    <h4>Contact Us</h4>
    <div class="cols">
      <p>Ola Haugtun<br>Lot 4 Elmer Road,<br>Harwick, SA, 5160<br>PO Box 212,<br>Harwick, SA, 5160</p>
      <p>Phone Work/Mobile: 0400 555 218<br>Phone: 08 5550 1742<br>Fax: 08 55501743<br>Email: ola@tindrafence.com</p>
    </div>
  </div>
  <p class="copyright">© 2012 Brightvale Provisions. All Rights Reserved.</p>
</footer>

</body>
</html>
```